Owen Tasker Studios Business Card

Looking for a clear, modern, elegant, sharp business card that conveys a professional yet edgy image to my business as a wedding, portrait, and travel photographer. Would like something that looks vintage yet modern. Need a new business card to grow my business. We are growing the business for Wedding and Event Photography as well as fine art Photography. (Mostly Landscapes)
Updates

I’m looking through designs now but I have a new logo that i want using please.

New logo uploaded please redesign using that

PLEASE ALL DESIGNERS LOOK IN BRIEF FOR NEW LOGO

Target Market(s)

Brides, Grooms, Families with Kids, People looking for Fine Art Photography Artwork

Industry/Entity Type

Photographer

Contact Information for Business Card

Unsure

Font styles to use
Serif

Colors

Designer to choose colors to be used in the design.

Requirements
Must have
• My Website:
• http://taskerlens.examplefolio.net
• Phone:
• 323-481-5206
• Email:
• owentaskerlens@mailbox-example.net
Nice to have
• Would like a sort of shine on the printing finish.
• I like black I think it looks good on a business card.
• Can try working with my logo (png that I've attached)

```html
<!DOCTYPE html>
<html lang="en">
<head>
<meta charset="utf-8">
<title>Owen Tasker Studios – Business Card</title>
<link rel="stylesheet" href="https://fonts.googleapis.com/css2?family=Raleway:wght@300;400&display=swap">
<style>
  :root {
    --backdrop: #dcdcdc;
    --card-white: #ffffff;
    --card-black: #17171a;
    --ink-dark: #2a2a2a;
    --ink-silver: #b8b8bc;
    --card-shadow: rgba(0, 0, 0, 0.18);
  }
  * { margin: 0; padding: 0; box-sizing: border-box; }
  html, body {
    width: 1200px;
    height: 800px;
    overflow: hidden;
    background: var(--backdrop);
  }
  .canvas {
    width: 1200px;
    height: 800px;
    display: flex;
    align-items: center;
    justify-content: center;
    gap: 60px;
    font-family: "Raleway", sans-serif;
  }
  .card {
    width: 520px;
    height: 297px;
    border-radius: 26px;
    box-shadow: 0 6px 18px var(--card-shadow);
    position: relative;
    overflow: hidden;
  }
  .card--back {
    background: var(--card-white);
    color: var(--ink-dark);
  }
  .card--front {
    background: var(--card-black);
    display: flex;
    align-items: center;
    justify-content: center;
  }
  .contact {
    position: absolute;
    left: 0;
    right: 0;
    top: 104px;
    text-align: center;
    font-size: 13px;
    font-weight: 400;
    letter-spacing: 1.4px;
    line-height: 24px;
  }
  .contact__sep {
    margin: 0 9px;
  }
  .contact__social-mark {
    display: inline-block;
    width: 10px;
    height: 10px;
    background: var(--ink-dark);
    border-radius: 2px;
    margin-right: 3px;
    vertical-align: -1px;
  }
  .wordmark {
    text-align: center;
    color: var(--ink-silver);
    font-weight: 300;
  }
  .wordmark__name {
    font-size: 27px;
    letter-spacing: 9px;
    margin-right: -9px;
    line-height: 1;
  }
  .wordmark__studios {
    font-size: 8px;
    letter-spacing: 6px;
    margin-right: -6px;
    margin-top: 8px;
  }
</style>
</head>
<body>
  <main class="canvas">
    <section class="card card--back" aria-label="Business card back">
      <div class="contact">
        <p class="contact__line">
          <span class="contact__phone">323-481-5206</span><span class="contact__sep">|</span><span class="contact__email">owentaskerlens@mailbox-example.net</span>
        </p>
        <p class="contact__line">
          <span class="contact__web">taskerlens.examplefolio.net</span><span class="contact__sep">|</span><span class="contact__social"><span class="contact__social-mark"></span>@owentaskerlens</span>
        </p>
      </div>
    </section>

    <section class="card card--front" aria-label="Business card front">
      <div class="wordmark">
        <p class="wordmark__name">OWEN TASKER</p>
        <p class="wordmark__studios">STUDIOS</p>
      </div>
    </section>
  </main>
</body>
</html>
```